Book Cover Design for a Novella

This book is a whimsical book about random philosophical thoughts. The size of the book is 4X6 inches, about 140 pages long. I would like the background color to be maroon. The title of the book is The Velvet Almanac of a Borrowed Lantern, and the author name is Nora Penwick. I would like the lettering to either be black or gold, in a font that looks like handwriting. From the lower left corner of the front cover, I would like there to be a gold-colored gardenia.
On the back cover, this is the book summary/description: “We are meant to share our hearts, not give them away. Vulnerability is not the act of placing your heart in someone else’s hands, saying, ‘Keep this safe for me.’ Vulnerability is wearing your heart on your sleeve, showing others your beauty, truths, and fears, and trusting that they will respect you.”
For the author's bio: Nora Penwick is a native of Boulder, Colorado. She enjoys spending time with her cats, eating pasta, and contemplating random things, such as banana spiders, sewage systems, and other huge things that scare her.
I would like all the writing on the back to be in a black, regular font.
I will upload the author's photo, which I would like to be put next to the bio, and I will also attach a rough sketch of what I'd like the cover to look like. Message me with any questions! Thanks.

```html
<!DOCTYPE html>
<html lang="en">
<head>
<meta charset="utf-8">
<title>The Velvet Almanac of a Borrowed Lantern — Cover</title>
<link rel="stylesheet" href="https://fonts.googleapis.com/css2?family=Marcellus+SC&family=Arimo:wght@400;700&display=swap">
<style>
  :root {
    --maroon-core: #b3021c;
    --maroon-edge: #780010;
    --gold: #e9c55c;
    --gold-soft: rgba(233, 197, 92, 0.35);
    --ink: #140204;
    --photo-tone: #9a8f86;
  }
  html, body {
    margin: 0;
    padding: 0;
    width: 1200px;
    height: 870px;
    overflow: hidden;
  }
  .cover {
    position: relative;
    width: 1200px;
    height: 870px;
    background: radial-gradient(ellipse 70% 75% at 50% 50%, var(--maroon-core) 0%, #9a0016 55%, var(--maroon-edge) 100%);
    overflow: hidden;
  }
  .back-quote {
    position: absolute;
    left: 72px;
    top: 142px;
    width: 442px;
    margin: 0;
    font-family: "Arimo", Arial, sans-serif;
    font-size: 17.6px;
    line-height: 35.2px;
    color: var(--ink);
    text-align: justify;
  }
  .author-photo {
    position: absolute;
    left: 72px;
    top: 511px;
    width: 120px;
    height: 171px;
    background: linear-gradient(160deg, #c9c2b8 0%, var(--photo-tone) 55%, #3a302c 100%);
    box-shadow: 0 0 0 1px rgba(0,0,0,0.25);
  }
  .author-bio {
    position: absolute;
    left: 206px;
    top: 504px;
    width: 309px;
    margin: 0;
    font-family: "Arimo", Arial, sans-serif;
    font-size: 17.6px;
    line-height: 26.8px;
    color: var(--ink);
    text-align: justify;
  }
  .author-bio .bio-name {
    color: var(--gold);
    font-weight: 700;
  }
  .spine {
    position: absolute;
    left: 584px;
    top: 22px;
    height: 830px;
    width: 30px;
    writing-mode: vertical-rl;
    font-family: "Marcellus SC", "Cinzel", serif;
    color: var(--gold);
    font-size: 21px;
    line-height: 30px;
    white-space: nowrap;
    display: flex;
    justify-content: space-between;
  }
  .spine-title { letter-spacing: 0.6px; }
  .spine-author { letter-spacing: 1px; }
  .front-title {
    position: absolute;
    left: 660px;
    top: 44px;
    width: 500px;
    margin: 0;
    font-family: "Marcellus SC", "Cinzel", serif;
    font-weight: 400;
    font-size: 43px;
    line-height: 54px;
    color: var(--gold);
    text-align: center;
    letter-spacing: 1px;
  }
  .front-title span { display: block; }
  .front-art {
    position: absolute;
    left: 620px;
    top: 318px;
    width: 340px;
    height: 485px;
  }
  .front-author {
    position: absolute;
    left: 660px;
    top: 790px;
    width: 500px;
    margin: 0;
    font-family: "Marcellus SC", "Cinzel", serif;
    font-size: 43px;
    line-height: 54px;
    color: var(--gold);
    text-align: center;
    letter-spacing: 1.5px;
  }
</style>
</head>
<body>
<main class="cover">
  <p class="back-quote">“We are meant to share our hearts, not give them away. Vulnerability is not the act of placing your heart in someone else’s hands, saying, ‘Keep this safe for me. ’Vulnerability is wearing your heart on your sleeve, showing others your beauty, truths, and fears, and trusting that they will respect you.”</p>

  <div class="author-photo" role="img" aria-label="Author portrait photograph"></div>
  <p class="author-bio"><span class="bio-name">Nora Penwick</span> is a native of Boulder, Colorado. She enjoys spending time with her cats, eating pasta, and contemplating random things, such as banana spiders, sewage systems, and other huge things that scare her.</p>

  <div class="spine">
    <span class="spine-title">The Velvet Almanac of a Borrowed Lantern</span>
    <span class="spine-author">Nora Penwick</span>
  </div>

  <h1 class="front-title">
    <span>The</span>
    <span>Velvet Almanac</span>
    <span>of a</span>
    <span>Borrowed Lantern</span>
  </h1>

  <svg class="front-art" viewBox="0 0 340 485" role="img" aria-label="Gold line drawing of a flower on a long stem rising from the lower left">
    <defs>
      <radialGradient id="bloomGlow" cx="60%" cy="30%" r="60%">
        <stop offset="0%" stop-color="var(--gold)" stop-opacity="0.35"/>
        <stop offset="100%" stop-color="var(--gold)" stop-opacity="0"/>
      </radialGradient>
    </defs>
    <rect x="0" y="0" width="340" height="485" fill="url(#bloomGlow)"/>
  </svg>

  <p class="front-author">Nora Penwick</p>
</main>
</body>
</html>
```